Inspirational quote for home gym wall - Desmond Ruiz quote

I'd like to design a poster for my home gym with a quote from Desmond Ruiz

"The fight is won or lost far away from witnesses - behind the lines, in the gym, and out there on the road, long before I dance under those lights."

The size should be approximately 1.5 x 2 m.

It's for inspiration to keep me going in my gym and there's noone better than Ruiz. I will get it printed onto canvas. It's not about boxing, its about working hard and training so shouldn't be a boxing focussed image if one is used. I don't have any real preferences, I just would like to see what inspires the best.

Font styles to use
Sans Serif

Colors
000000
ffffff
fbed33

Requirements
Nice to have
• Maybe a black and white image of Ruiz training in the background?
• Some thoughts on type of images (doesn't have to be these ones)
• https://www.stockvalemedia.example/detail/photo/heavyweight-champion-desmond-ruiz-training/10482937
• https://www.findorasearch.example/images?q=desmond+ruiz+training&filter=weight+lifting#img1
• https://www.findorasearch.example/images?q=desmond+ruiz+training#img2
• https://www.findorasearch.example/images?q=desmond+ruiz+training#img3
• https://www.findorasearch.example/images?q=desmond+ruiz+training#img4
• https://www.findorasearch.example/images?q=desmond+ruiz+training#img5
• The more designs I see, the more I prefer black and white with maybe only a bit of colour such as gold.
Should not have
• I'm not a fan of red

```html
<!DOCTYPE html>
<html lang="en">
<head>
<meta charset="utf-8">
<title>Desmond Ruiz — Training Quote Poster</title>
<link href="https://fonts.googleapis.com/css2?family=Jost:wght@300&display=swap" rel="stylesheet">
<style>
  :root {
    --ink: #000000;
    --paper: #ffffff;
    --photo-light: #8c8c8c;
    --photo-dark: #3a3a3a;
  }
  html, body {
    margin: 0;
    padding: 0;
    width: 900px;
    height: 1200px;
    overflow: hidden;
    background: var(--ink);
  }
  .poster {
    position: relative;
    width: 900px;
    height: 1200px;
    background: var(--ink);
  }
  .poster__photo {
    position: absolute;
    left: 0;
    top: 0;
    width: 900px;
    height: 559px;
    background: linear-gradient(180deg, var(--photo-light) 0%, var(--photo-dark) 100%);
  }
  .poster__quote {
    position: absolute;
    left: 52px;
    top: 598px;
    width: 794px;
    margin: 0;
    font-family: "Jost", "Futura", sans-serif;
    font-weight: 300;
    font-size: 76px;
    line-height: 85.6px;
    color: var(--paper);
  }
  .poster__line {
    display: block;
    text-align: justify;
    text-align-last: justify;
    white-space: nowrap;
  }
  .poster__line--tight {
    letter-spacing: -0.01em;
    word-spacing: -0.14em;
  }
  .poster__line--last {
    text-align: left;
    text-align-last: left;
  }
</style>
</head>
<body>
  <main class="poster">
    <div class="poster__photo" role="img" aria-label="Black and white photograph of Desmond Ruiz training in a gym"></div>
    <blockquote class="poster__quote">
      <span class="poster__line">“The fight is won or lost</span>
      <span class="poster__line">far away from witnesses</span>
      <span class="poster__line">- behind the lines, in the</span>
      <span class="poster__line poster__line--tight">gym, and out there on the</span>
      <span class="poster__line poster__line--tight">road, long before I dance</span>
      <span class="poster__line poster__line--last">under those lights.”</span>
    </blockquote>
  </main>
</body>
</html>
```